BRAMBLE Underwriting Trade Show Banner Insurance Underwriting

WE need a design for a trade show banner. BRAMBLE Underwriting Inc. is an independently Canadian owned boutique Managing General Agent that brings unequalled value to our three customers:
​Tailored insurance coverage and products for individual insureds​Support and industry knowledge for our broker partners​
Expert underwriting for our insurance carriers. Our website is https://www.brambleunderwriting.example. We would like to keep the font the same. I've put more instructions in a word document attached. We want it to flow with our fact sheets. I'm also adding our colors for our logo.

```html
<!DOCTYPE html>
<html lang="en">
<head>
<meta charset="utf-8">
<title>BRAMBLE Underwriting – Pull-up Banners</title>
<link href="https://fonts.googleapis.com/css2?family=Montserrat:wght@500;700&family=Noto+Sans:wght@800&family=Fira+Sans+Condensed:wght@500&family=Fira+Sans+Extra+Condensed:ital,wght@0,500;1,500;1,700&display=swap" rel="stylesheet">
<style>
  :root {
    --navy: #1c2b5a;
    --steel: #9eabb3;
    --tile-band: #a9b3ba;
    --ink: #111111;
    --paper: #ffffff;
    --stage: #8d8d90;
    --badge-dark: #111111;
    --badge-red: #d8283c;
  }
  * { box-sizing: border-box; margin: 0; padding: 0; }
  html, body {
    width: 1187px; height: 1200px; overflow: hidden;
    background: var(--stage);
  }
  .canvas { position: relative; width: 1187px; height: 1200px; }

  .banner {
    position: absolute; top: 120px; width: 383px; height: 927px;
    background: var(--paper); overflow: hidden;
    box-shadow: 4px 6px 10px rgba(0,0,0,0.25);
  }
  .banner--about { left: 166px; }
  .banner--products { left: 632px; }

  .wordmark {
    position: absolute; top: 86px; left: 0; width: 100%;
    display: flex; align-items: center; justify-content: center; gap: 9px;
    font-family: "Montserrat", sans-serif; font-weight: 700;
    font-size: 21px; line-height: 26px; color: var(--navy); letter-spacing: 0.3px;
  }
  .wordmark__square { width: 14px; height: 14px; background: var(--navy); }

  .headline {
    position: absolute; left: 0; width: 100%; text-align: center;
    font-family: "Noto Sans", sans-serif; font-weight: 800;
    color: var(--navy); line-height: 36px;
  }
  .banner--about .headline { top: 174px; font-size: 28px; }
  .banner--products .headline { top: 174px; font-size: 31px; }

  .rule { position: absolute; height: 2px; background: var(--navy); }
  .banner--about .rule { top: 294px; left: 39px; width: 305px; }
  .banner--products .rule { top: 226px; left: 38px; width: 305px; }

  .intro {
    position: absolute; top: 306px; left: 0; width: 100%; text-align: center;
    font-family: "Fira Sans Condensed", sans-serif; font-weight: 500;
    font-size: 22px; line-height: 26px; color: var(--ink);
  }

  .hero-photo {
    position: absolute; top: 383px; left: 0; width: 100%; height: 460px;
    background: linear-gradient(160deg, #f6f6f6 0%, #d4d4d4 28%, #8c8c8c 48%, #4a4a4a 60%, #a7a7a7 74%, #e6e6e6 86%, #f6f6f6 100%);
  }

  .tagline {
    position: absolute; left: 0; width: 100%; text-align: center;
    font-family: "Fira Sans Extra Condensed", sans-serif; font-style: italic;
    font-weight: 500; font-size: 24px; line-height: 24px; color: var(--navy);
  }
  .tagline strong { font-weight: 700; }
  .banner--about .tagline { top: 728px; }
  .banner--products .tagline { top: 771px; }

  .affiliations {
    position: absolute; top: 792px; left: 40px; right: 44px;
    display: flex; align-items: center; justify-content: space-between;
  }
  .coverholder {
    display: flex; align-items: center; gap: 5px;
    font-family: "Montserrat", sans-serif; font-weight: 500; font-size: 11px; color: var(--ink);
  }
  .coverholder__badge { width: 67px; height: 26px; background: var(--badge-dark); }
  .association { display: flex; align-items: center; gap: 5px; }
  .association__badge { width: 34px; height: 34px; border-radius: 50%; background: var(--badge-red); }
  .association__name {
    font-family: "Montserrat", sans-serif; font-weight: 700; font-size: 5.5px;
    line-height: 7px; color: var(--ink);
  }

  .footer-band {
    position: absolute; bottom: 0; left: 0; width: 100%; height: 84px;
    background: var(--navy); color: var(--paper);
    font-family: "Montserrat", sans-serif; font-weight: 500; font-size: 18px;
    text-align: center; padding-top: 17px;
  }
  .footer-band strong { font-weight: 700; }

  .product-grid {
    position: absolute; top: 255px; left: 28px;
    display: grid; grid-template-columns: 156px 156px; column-gap: 14px;
    grid-template-rows: 142px 142px 142px; row-gap: 25px;
  }
  .product-tile {
    position: relative; border: 1.5px solid var(--navy); border-radius: 9px;
    overflow: hidden; box-shadow: 0 4px 4px rgba(0,0,0,0.18);
    display: flex; flex-direction: column;
  }
  .product-tile__photo { flex: 1; }
  .product-tile__label {
    background: var(--tile-band); text-align: center; color: var(--ink);
    font-family: "Fira Sans Extra Condensed", sans-serif; font-weight: 500;
    font-size: 16px; line-height: 16px; padding: 4px 2px 3px;
  }
  .photo--stethoscope { background: linear-gradient(150deg, #f2f2f2 0%, #b8b8b8 30%, #6e6e6e 50%, #c8c8c8 70%, #f4f4f4 100%); }
  .photo--dishes { background: linear-gradient(180deg, #f4f4f4 0%, #dcdcdc 45%, #c2c2c2 65%, #eeeeee 100%); }
  .photo--conveyor { background: linear-gradient(180deg, #f6f6f6 0%, #e6e6e6 35%, #555555 52%, #9a9a9a 62%, #efefef 85%); }
  .photo--camera { background: linear-gradient(160deg, #dcdcdc 0%, #8f8f8f 30%, #262626 55%, #3c3c3c 75%, #b5b5b5 100%); }
  .photo--figures { background: linear-gradient(90deg, #ececec 0%, #a9a9a9 28%, #e8e8e8 50%, #a9a9a9 72%, #ececec 100%); }
  .photo--salon { background: linear-gradient(90deg, #5c5c5c 0%, #dadada 22%, #777777 45%, #d6d6d6 62%, #2a2a2a 82%, #111111 100%); }
</style>
</head>
<body>
<div class="canvas">

  <section class="banner banner--about">
    <div class="hero-photo" role="img" aria-label="Black and white photo of two hands fitting together a navy and a grey puzzle piece over a desk"></div>
    <div class="wordmark"><span class="wordmark__square"></span>BRAMBLE Underwriting</div>
    <h1 class="headline">Customer Focused.<br>Expert Knowledge.<br>Integrity.</h1>
    <div class="rule"></div>
    <p class="intro">We are an independently<br>owned specialist Managing<br>General Agent.</p>
    <p class="tagline">Make <strong>BRAMBLE Underwriting</strong><br>your competitive advantage!</p>
    <div class="affiliations">
      <div class="coverholder">Coverholder at <span class="coverholder__badge"></span></div>
      <div class="association">
        <span class="association__badge"></span>
        <span class="association__name">Northern Guild of<br>Managing General Agents</span>
      </div>
    </div>
    <div class="footer-band">www.<strong>brambleunderwriting</strong>.example</div>
  </section>

  <section class="banner banner--products">
    <div class="wordmark"><span class="wordmark__square"></span>BRAMBLE Underwriting</div>
    <h2 class="headline">Our Products</h2>
    <div class="rule"></div>
    <div class="product-grid">
      <div class="product-tile">
        <div class="product-tile__photo photo--stethoscope" role="img" aria-label="Close-up of a stethoscope"></div>
        <div class="product-tile__label">Healthcare</div>
      </div>
      <div class="product-tile">
        <div class="product-tile__photo photo--dishes" role="img" aria-label="Stacked glass petri dishes"></div>
        <div class="product-tile__label">Life Sciences</div>
      </div>
      <div class="product-tile">
        <div class="product-tile__photo photo--conveyor" role="img" aria-label="Industrial conveyor belt"></div>
        <div class="product-tile__label">Manufacturing &amp;<br>Wholesale</div>
      </div>
      <div class="product-tile">
        <div class="product-tile__photo photo--camera" role="img" aria-label="Professional camera in a photo studio"></div>
        <div class="product-tile__label">Media E &amp; O</div>
      </div>
      <div class="product-tile">
        <div class="product-tile__photo photo--figures" role="img" aria-label="Two wooden mannequin figures facing each other"></div>
        <div class="product-tile__label">Misc. E &amp; O</div>
      </div>
      <div class="product-tile">
        <div class="product-tile__photo photo--salon" role="img" aria-label="Hair salon tools: brush, clips, scissors and spray bottle"></div>
        <div class="product-tile__label">Spas &amp; Salons</div>
      </div>
    </div>
    <p class="tagline">Make <strong>BRAMBLE Underwriting</strong><br>your competitive advantage!</p>
    <div class="footer-band">www.<strong>brambleunderwriting</strong>.example</div>
  </section>

</div>
</body>
</html>
```